Business Management Fortress

Assist with enhancing a powerpoint slide by providing a few design options for consideration. I have a template but open to any creative ideas.

Target Market(s)

Internal employees and stakeholders

Industry/Entity Type

Business Management, Finance, Accounting

Requirements
Must have
• Maintain a fortress, temple, or pyramid schema
Nice to have
• Scenic Background

```html
<!DOCTYPE html>
<html lang="en">
<head>
<meta charset="utf-8">
<title>Business Management Fortress</title>
<link href="https://fonts.googleapis.com/css2?family=Figtree:wght@400;500;700&display=swap" rel="stylesheet">
<style>
  :root {
    --navy: #1f4a78;
    --navy-deep: #113b63;
    --divider: #c7dcf0;
    --ink-light: #ffffff;
    --sky-top: #bcd9f1;
    --sky-mid: #c9c2ad;
    --forest: #8d9a78;
    --lake: #a6cfe6;
  }
  html, body {
    margin: 0;
    padding: 0;
    width: 1200px;
    height: 675px;
    overflow: hidden;
    background: #ffffff;
  }
  .slide {
    position: relative;
    width: 1200px;
    height: 675px;
    overflow: hidden;
    font-family: "Figtree", sans-serif;
  }
  .scenic-backdrop {
    position: absolute;
    inset: 0;
    background:
      linear-gradient(180deg,
        var(--sky-top) 0%,
        #cfd6d8 18%,
        var(--sky-mid) 34%,
        var(--forest) 52%,
        #b9c5ad 56%,
        #b8cdc8 70%,
        var(--lake) 100%);
    opacity: 0.85;
  }
  .fortress {
    position: absolute;
    inset: 0;
    width: 1200px;
    height: 675px;
  }
  .roof, .entablature, .column-shaft, .plinth { fill: var(--navy); }
  .entablature-rim, .column-cap, .column-base { fill: var(--navy-deep); }
  .roof-divider { stroke: var(--divider); stroke-width: 2; }
  .icon { fill: var(--ink-light); }
  .icon-cut { fill: var(--navy); }
  .roof-label {
    fill: var(--ink-light);
    font-size: 19px;
    font-weight: 500;
    text-anchor: middle;
  }
  .pillar-label {
    fill: var(--ink-light);
    font-size: 23px;
    font-weight: 500;
  }
  .foundation-title {
    fill: var(--ink-light);
    font-size: 19px;
    font-weight: 700;
    text-anchor: middle;
  }
  .foundation-detail {
    fill: var(--ink-light);
    font-size: 14px;
    font-weight: 400;
    text-anchor: middle;
  }
</style>
</head>
<body>
<div class="slide">
  <div class="scenic-backdrop" role="img" aria-label="Faded photo of snow-capped mountains and forest reflected in a calm alpine lake"></div>

  <svg class="fortress" viewBox="0 0 1200 675" xmlns="http://www.w3.org/2000/svg">
    <!-- Roof -->
    <path class="roof" d="M597,63 Q590,60 582,64 L310,172 Q300,178 305,186 Q308,191 318,191 L880,191 Q890,191 892,184 Q894,176 884,172 L612,64 Q604,60 597,63 Z"/>
    <line class="roof-divider" x1="488" y1="103" x2="578" y2="192"/>
    <line class="roof-divider" x1="705" y1="103" x2="616" y2="192"/>

    <!-- Entablature -->
    <rect class="entablature" x="332" y="192" width="530" height="27" rx="10"/>
    <rect class="entablature-rim" x="332" y="192" width="530" height="8"/>

    <!-- Roof icons & labels -->
    <g class="icon" transform="translate(478,140)">
      <circle cx="0" cy="-11" r="4"/>
      <rect x="-5" y="-6" width="10" height="21" rx="3"/>
      <circle cx="-12" cy="-5" r="3"/>
      <rect x="-16" y="-1" width="8" height="14" rx="2.5"/>
      <circle cx="13" cy="-5" r="3"/>
      <rect x="9" y="-1" width="8" height="14" rx="2.5"/>
      <rect x="-1" y="-21" width="2" height="5"/>
      <rect x="-8" y="-19" width="2" height="4" transform="rotate(-30 -7 -17)"/>
      <rect x="6" y="-19" width="2" height="4" transform="rotate(30 7 -17)"/>
    </g>
    <text class="roof-label" x="476" y="184">Leaders</text>

    <g class="icon" transform="translate(597,114)">
      <rect x="-19" y="-12" width="8" height="14" rx="1.5" transform="rotate(-25 -15 -5)"/>
      <rect x="11" y="-12" width="8" height="14" rx="1.5" transform="rotate(25 15 -5)"/>
      <path d="M-12,-6 L-2,-10 L8,-6 L12,2 L2,12 L-6,12 L-13,4 Z"/>
      <path class="icon-cut" d="M-3,-6 L4,-3 L-2,2 Z"/>
    </g>
    <text class="roof-label" x="597" y="150">Partner</text>

    <g class="icon" transform="translate(721,140)">
      <path d="M-4,-16 L4,-16 L2,-11 Q12,-6 11,3 Q10,8 0,8 Q-10,8 -11,3 Q-12,-6 -2,-11 Z"/>
      <text x="0" y="3" fill="#1f4a78" font-size="10" font-weight="700" text-anchor="middle" font-family="Figtree, sans-serif">$</text>
      <path d="M-20,6 Q-12,4 -6,8 L8,8 Q14,6 18,4 L20,6 Q14,14 4,16 L-10,16 L-16,22 L-21,17 Z"/>
    </g>
    <text class="roof-label" x="725" y="182">Profitability</text>

    <!-- Pillars -->
    <g transform="translate(400,0)">
      <rect class="column-cap" x="-41" y="228" width="82" height="14" rx="7"/>
      <path class="column-shaft" d="M-30,242 Q-42,375 -33,508 L33,508 Q42,375 30,242 Z"/>
      <rect class="column-base" x="-36" y="507" width="72" height="14" rx="7"/>
      <g class="icon" transform="translate(-1,312)">
        <circle cx="-11" cy="-9" r="5"/><circle cx="11" cy="-9" r="5"/><circle cx="0" cy="-6" r="6"/>
        <path d="M-21,8 Q-21,-2 -11,-2 Q-4,-2 -3,3 L-3,8 Z"/>
        <path d="M21,8 Q21,-2 11,-2 Q4,-2 3,3 L3,8 Z"/>
        <path d="M-11,15 Q-11,2 0,2 Q11,2 11,15 Z"/>
      </g>
      <text class="pillar-label" transform="translate(8,465) rotate(-90)">People</text>
    </g>

    <g transform="translate(530,0)">
      <rect class="column-cap" x="-41" y="228" width="82" height="14" rx="7"/>
      <path class="column-shaft" d="M-30,242 Q-42,375 -33,508 L33,508 Q42,375 30,242 Z"/>
      <rect class="column-base" x="-36" y="507" width="72" height="14" rx="7"/>
      <g class="icon" transform="translate(1,310)">
        <path d="M0,-18 Q-15,-18 -15,-3 Q-15,5 -7,11 L-7,15 L7,15 L7,11 Q15,5 15,-3 Q15,-18 0,-18 Z"/>
        <rect x="-6" y="17" width="12" height="3" rx="1"/>
        <rect x="-4" y="21" width="8" height="2" rx="1"/>
        <circle class="icon-cut" cx="5" cy="-3" r="5"/>
        <circle cx="5" cy="-3" r="2.5"/>
      </g>
      <text class="pillar-label" transform="translate(8,465) rotate(-90)">Innovation</text>
    </g>

    <g transform="translate(663,0)">
      <rect class="column-cap" x="-37" y="228" width="74" height="14" rx="7"/>
      <path class="column-shaft" d="M-30,242 Q-40,375 -33,508 L33,508 Q40,375 30,242 Z"/>
      <rect class="column-base" x="-36" y="507" width="72" height="14" rx="7"/>
      <g class="icon" transform="translate(-4,310)">
        <path d="M-2,-20 Q-20,-20 -22,-4 Q-22,12 -6,20 L4,20 L4,-20 Z"/>
        <path class="icon-cut" d="M-12,-10 Q-6,-6 -12,0 M-16,6 Q-8,4 -4,10" stroke="#1f4a78" stroke-width="2" fill="none"/>
        <rect x="4" y="-9" width="12" height="2"/>
        <rect x="4" y="0" width="18" height="2"/>
        <rect x="4" y="9" width="10" height="2"/>
        <rect x="15" y="-18" width="2" height="10"/>
        <circle cx="16" cy="-19" r="3"/><circle cx="23" cy="1" r="3"/><circle cx="15" cy="18" r="3"/>
        <rect x="13" y="9" width="2" height="8"/>
      </g>
      <text class="pillar-label" transform="translate(661,465) rotate(-90)" dx="0" style="transform:none"></text>
    </g>
    <text class="pillar-label" transform="translate(661,465) rotate(-90)">Business</text>
    <text class="pillar-label" transform="translate(682,465) rotate(-90)">Intelligence</text>

    <g transform="translate(794,0)">
      <rect class="column-cap" x="-37" y="228" width="74" height="14" rx="7"/>
      <path class="column-shaft" d="M-30,242 Q-40,375 -33,508 L33,508 Q40,375 30,242 Z"/>
      <rect class="column-base" x="-36" y="507" width="72" height="14" rx="7"/>
      <g class="icon" transform="translate(0,312)">
        <circle cx="0" cy="-19" r="4"/>
        <path d="M-4,-15 L4,-15 L3,-6 L6,-2 L-6,-2 L-3,-6 Z"/>
        <rect x="-19" y="-4" width="7" height="11" rx="1" transform="rotate(-25 -15 1)"/>
        <rect x="12" y="-4" width="7" height="11" rx="1" transform="rotate(25 15 1)"/>
        <path d="M-13,1 L-4,-1 L5,-1 L13,3 L4,12 L-4,12 L-12,6 Z"/>
      </g>
      <text class="pillar-label" transform="translate(793,465) rotate(-90)" style="display:none"></text>
    </g>
    <text class="pillar-label" transform="translate(793,465) rotate(-90)">Strategic</text>
    <text class="pillar-label" transform="translate(814,465) rotate(-90)">Alliances</text>

    <!-- Foundation -->
    <path class="plinth" d="M342,540 Q342,530 352,530 L841,530 Q851,530 851,540 L851,560 L882,560 Q890,560 890,568 L890,615 Q890,623 882,623 L312,623 Q304,623 304,615 L304,568 Q304,560 312,560 L342,560 Z"/>
    <text class="foundation-title" x="597" y="560">Fiduciary Responsibilities</text>
    <text class="foundation-detail" x="597" y="587">Accurate Financials/Internal Controls/Brand Protection</text>
    <text class="foundation-detail" x="597" y="606">Compliance/Ethics/Cost Management</text>
  </svg>
</div>
</body>
</html>
```